Business card for medical clinic

I need an upmarket, modern medical/health business card for my clinic

Contact Information for Business Card

name, address, email, qr code

```html
<!DOCTYPE html>
<html lang="en">
<head>
<meta charset="utf-8">
<title>Meridia Care Clinic – Business Card</title>
<link href="https://fonts.googleapis.com/css2?family=Outfit:wght@300;400;700&display=swap" rel="stylesheet">
<style>
  :root {
    --brand-blue: #139acd;
    --card-light: #f0f1f3;
    --page-bg: #ffffff;
    --white: #ffffff;
  }
  * { margin: 0; padding: 0; box-sizing: border-box; }
  html, body {
    width: 1200px; height: 1200px; overflow: hidden;
    background: var(--page-bg);
    font-family: "Outfit", sans-serif;
  }
  .canvas { position: relative; width: 1200px; height: 1200px; }

  .card {
    position: absolute; left: 121px; width: 966px; height: 569px; overflow: hidden;
  }
  .card--front { top: 29px; background: var(--card-light); }
  .card--back { top: 609px; background: var(--brand-blue); }

  /* front */
  .accent-bar {
    position: absolute; left: 0; top: 43px; width: 307px; height: 17px;
    background: var(--brand-blue); border-radius: 0 9px 9px 0;
  }
  .holder-name {
    position: absolute; left: 37px; top: 78px;
    font-size: 46px; font-weight: 700; color: var(--brand-blue); letter-spacing: 0.5px;
  }
  .holder-position {
    position: absolute; left: 0; width: 279px; top: 126px; text-align: right;
    font-size: 26px; font-weight: 300; color: var(--brand-blue);
  }
  .side-pill {
    position: absolute; left: 851px; width: 59px; height: 97px; background: var(--brand-blue);
  }
  .side-pill--top { top: 0; border-radius: 0 0 30px 30px; }
  .side-pill--bottom { top: 472px; border-radius: 30px 30px 0 0; }

  .contact-list { list-style: none; }
  .contact-item {
    position: absolute; left: 467px; width: 443px; height: 40px;
    display: flex; align-items: center; justify-content: space-between;
  }
  .contact-text { font-size: 28px; font-weight: 300; color: var(--brand-blue); white-space: nowrap; }
  .contact-icon {
    width: 59px; height: 40px; border-radius: 20px; background: var(--brand-blue);
    display: flex; align-items: center; justify-content: center;
  }
  .contact-icon svg { width: 26px; height: 26px; }

  .brand-front {
    position: absolute; left: 57px; top: 412px;
    display: flex; align-items: center; gap: 14px; color: var(--brand-blue);
  }
  .brand-mark {
    width: 70px; height: 70px; border-radius: 50%; border: 4px solid currentColor;
  }
  .brand-name { font-weight: 400; line-height: 1.1; letter-spacing: 2px; }
  .brand-front .brand-name { font-size: 24px; }

  /* back */
  .center-pill {
    position: absolute; left: 454px; width: 59px; background: var(--card-light);
  }
  .center-pill--top { top: 0; height: 110px; border-radius: 0 0 30px 30px; }
  .center-pill--bottom { top: 457px; height: 112px; border-radius: 30px 30px 0 0; }
  .brand-back {
    position: absolute; left: 0; right: 0; top: 199px;
    display: flex; align-items: center; justify-content: center; gap: 26px; color: var(--white);
  }
  .brand-back .brand-mark { width: 150px; height: 150px; border-width: 6px; }
  .brand-back .brand-name { font-size: 42px; }
</style>
</head>
<body>
<main class="canvas">
  <section class="card card--front" aria-label="Card front">
    <div class="accent-bar"></div>
    <h1 class="holder-name">FULL NAME</h1>
    <p class="holder-position">Position</p>
    <div class="side-pill side-pill--top"></div>
    <div class="side-pill side-pill--bottom"></div>

    <ul class="contact-list">
      <li class="contact-item" style="top:157px">
        <span class="contact-text">+123-456-7890</span>
        <span class="contact-icon">
          <svg viewBox="0 0 24 24" fill="#fff"><path d="M6.6 10.8c1.4 2.8 3.8 5.1 6.6 6.6l2.2-2.2c.3-.3.7-.4 1-.2 1.1.4 2.3.6 3.6.6.6 0 1 .4 1 1V20c0 .6-.4 1-1 1C10.6 21 3 13.4 3 4c0-.6.4-1 1-1h3.5c.6 0 1 .4 1 1 0 1.3.2 2.5.6 3.6.1.3 0 .7-.2 1z"/></svg>
        </span>
      </li>
      <li class="contact-item" style="top:230px">
        <span class="contact-text">hello@reallygreatsite.com</span>
        <span class="contact-icon">
          <svg viewBox="0 0 24 24" fill="none" stroke="#fff" stroke-width="1.6"><rect x="2" y="5" width="20" height="14"/><path d="M2 5l10 8 10-8M2 19l7.5-7M22 19l-7.5-7"/></svg>
        </span>
      </li>
      <li class="contact-item" style="top:299px">
        <span class="contact-text">www.reallygreatsite.com</span>
        <span class="contact-icon">
          <svg viewBox="0 0 24 24" fill="none" stroke="#fff" stroke-width="1.6"><circle cx="12" cy="12" r="10"/><ellipse cx="12" cy="12" rx="4.5" ry="10"/><path d="M2 12h20M4 7h16M4 17h16"/></svg>
        </span>
      </li>
      <li class="contact-item" style="top:369px">
        <span class="contact-text">123 Anywhere St., Any City</span>
        <span class="contact-icon">
          <svg viewBox="0 0 24 24" fill="#fff"><path d="M12 2a7 7 0 0 0-7 7c0 5 7 13 7 13s7-8 7-13a7 7 0 0 0-7-7zm0 9.5A2.5 2.5 0 1 1 12 6.5a2.5 2.5 0 0 1 0 5z"/></svg>
        </span>
      </li>
    </ul>

    <div class="brand-front">
      <span class="brand-mark"></span>
      <span class="brand-name">MERIDIA CARE<br>CLINIC</span>
    </div>
  </section>

  <section class="card card--back" aria-label="Card back">
    <div class="center-pill center-pill--top"></div>
    <div class="center-pill center-pill--bottom"></div>
    <div class="brand-back">
      <span class="brand-mark"></span>
      <span class="brand-name">MERIDIA CARE<br>CLINIC</span>
    </div>
  </section>
</main>
</body>
</html>
```